Webdesign für IT Service Firma
Zielgruppe
Wir sind eine IT-Service Firma und bieten individuelle IT-Lösungen. Unsere Kunden sind KMU, also Firmen mit einer Grösse von 2-250 Mitarbeitern im Grossraum Basel, die in Ihrem Bereich Spezialisten sind und spezielle Anforderungen an Ihre IT besitzen.
Unsere USP sind fixe Ansprechpartner, gute Erreichbarkeit, schneller und individueller Service
Aufgabenstellung
Schriftart Myriad Pro
Grün: #7FA51D
Blau: #4D9BC2
Grau: #999999
Untertitel: Wir sind da.

```html
<!DOCTYPE html>
<html lang="de">
<head>
<meta charset="utf-8">
<title>NORVETA – IT Services aus Basel</title>
<link rel="stylesheet" href="https://fonts.googleapis.com/css2?family=Work+Sans:wght@400;500;600;700&display=swap">
<style>
:root{
  --green:#7FA51D;
  --blue:#4D9BC2;
  --blue-dark:#2e6788;
  --heading-blue:#2a6a8c;
  --grey:#999999;
  --text:#333a40;
  --cell-tint:#f7f9f1;
  --footer:#8399ae;
  --page:#eef1f5;
}
*{box-sizing:border-box;margin:0;padding:0}
html,body{width:1000px;height:1200px;overflow:hidden}
body{font-family:"Work Sans",Arial,sans-serif;color:var(--text);background:linear-gradient(160deg,#f4f6f9 0%,#e3e8ee 45%,#f5f7fa 100%);position:relative}
.abs{position:absolute}
.topbar{top:16px;left:195px;right:160px;height:22px;font-size:12.5px;color:var(--green)}
.topbar .item{position:absolute;top:2px;display:flex;align-items:center;gap:8px}
.lang{position:absolute;top:5px;font-size:8px;font-weight:700;color:var(--grey)}
.lang.active{color:var(--blue);background:#fff;border-radius:50%;width:22px;height:22px;top:-1px;display:flex;align-items:center;justify-content:center}
.header{top:53px;left:169px;width:662px;height:65px;background:#fff;border-radius:6px 6px 0 0}
.brand{position:absolute;left:26px;top:16px;display:flex;align-items:center;gap:6px;font-size:30px;font-weight:500;color:var(--blue);letter-spacing:1px}
.brand .dot{width:10px;height:10px;background:var(--green)}
.tagline{position:absolute;left:374px;top:28px;font-size:12.5px;color:var(--blue)}
.deco{position:absolute;right:0;top:0;width:140px;height:65px;background:linear-gradient(90deg,#fff,#cfe3ef 40%,#8cbcd6);border-radius:0 6px 0 0}
.nav{top:118px;left:169px;width:662px;height:36px;background:var(--blue);display:flex;padding-left:67px}
.nav a{color:#fff;font-weight:700;font-size:12.5px;text-decoration:none;padding:0 7.5px;line-height:36px}
.nav a.current{background:var(--blue-dark);height:39px}
.nav a:first-child{position:absolute;left:24px}
.hero-photo{top:154px;left:130px;width:300px;height:194px;background:linear-gradient(90deg,rgba(238,241,245,0) 0%,#c9cfd6 30%,#aeb7c0 60%,rgba(238,241,245,0) 100%)}
.hero-title{top:206px;left:424px;font-size:19px;font-weight:400;color:#222}
.hero-title strong{color:var(--blue);font-weight:600}
.hero-text{top:234px;left:426px;font-size:12.5px;line-height:18.3px;color:#222}
.grid{top:348px;left:147px;width:707px;height:482px}
.cell{position:absolute;width:236px;padding:38px 20px 0 48px;font-size:9.3px;line-height:13.5px}
.cell.tint{background:var(--cell-tint)}
.cell h3{font-size:9.3px;font-weight:700;color:var(--heading-blue);line-height:13.5px;margin-bottom:11px}
.cell-photo{background:linear-gradient(135deg,#d9dde1,#9aa3ab 55%,#e4e7ea)}
.band{top:832px;left:0;width:1000px;height:104px;background:radial-gradient(circle at 35% 60%,#86ad26,var(--green) 60%,#76991a)}
.band p{position:absolute;left:199px;top:42px;font-size:13px;color:#fff}
.band .btn{position:absolute;left:644px;top:33px;width:193px;height:38px;background:var(--blue-dark);color:#fff;font-size:13px;display:flex;align-items:center;justify-content:center}
.footer{top:936px;left:0;width:1000px;height:204px;background:var(--footer);color:#fff;font-size:9.3px}
.contact{position:absolute;left:215px;line-height:13.5px}
.contact b{font-weight:700}
.ficon{position:absolute;left:182px}
.svc-head{position:absolute;left:404px;top:47px;font-weight:700;font-size:9.3px}
.svc{position:absolute;list-style:none;line-height:20.8px}
.svc li::before{content:"›";margin-right:6px;font-size:12px}
.bottom{top:1140px;left:0;width:1000px;height:60px;background:#fff}
.bottom .brand{left:195px;top:18px;font-size:17px;gap:4px}
.bottom .brand .dot{width:6px;height:6px}
.legal{position:absolute;right:176px;top:25px;font-size:9.3px;color:var(--blue);display:flex;gap:10px}
</style>
</head>
<body>
<div class="abs topbar">
  <div class="item" style="left:0">
    <svg width="15" height="15" viewBox="0 0 24 24" fill="none" stroke="#4D9BC2" stroke-width="1.6"><path d="M5 3h4l2 5-2.5 1.5a11 11 0 0 0 6 6L16 13l5 2v4a2 2 0 0 1-2 2A16 16 0 0 1 3 5a2 2 0 0 1 2-2z"/></svg>
    +41 61 000 4821
  </div>
  <div class="item" style="left:144px">
    <svg width="15" height="12" viewBox="0 0 24 18" fill="none" stroke="#4D9BC2" stroke-width="1.6"><rect x="1" y="1" width="22" height="16" rx="1"/><path d="M1 2l11 8 11-8"/></svg>
    support@norveta.ch
  </div>
  <span class="lang active" style="left:566px">DE</span>
  <span class="lang" style="left:603px">EN</span>
</div>

<header class="abs header">
  <div class="brand"><span>NORVETA</span><span class="dot"></span></div>
  <div class="tagline">IT Services aus Basel</div>
  <div class="deco" role="img" aria-label="Dekorative Grafik: Leiterbahnen und Skyline von Basel"></div>
</header>
<nav class="abs nav">
  <a href="#">Home</a><a href="#" class="current">Leistungen</a><a href="#">Privatkunde?</a><a href="#">Jobs</a><a href="#">Hilfe</a><a href="#">Sozialprozent</a><a href="#">Über uns</a><a href="#">Kontakt</a>
</nav>

<div class="abs hero-photo" role="img" aria-label="Foto: zwei IT-Techniker mit Laptop im Serverraum"></div>
<h1 class="abs hero-title">Massgeschneiderte <strong>IT Dienstleistungen</strong></h1>
<p class="abs hero-text">Sie möchten eine IT, die Sie verstehen und bedienen können?<br>Wir bieten mehr als Hardware und Software: Wir bieten IT<br>als massgeschneiderte Dienstleistung.</p>

<section class="abs grid">
  <div class="cell" style="left:0;top:0;height:182px;background:#fff">
    <h3>Sie benötigen Beratung für<br>Ihre bestehende IT? Gibt es<br>Verbesserungsmöglichkeiten?</h3>
    <p>Gerne beraten wir Sie vor Ort<br>und sprechen über Ihre Ideen.</p>
  </div>
  <div class="cell tint" style="left:236px;top:0;height:182px;padding-left:46px">
    <h3>Sie möchten Hilfe bei grösseren<br>Beschaffungen und der<br>Bereitstellung dieser Geräte?</h3>
    <p>Wir beraten bei Hard- und<br>Software und installieren nach<br>Ihren Wünschen.</p>
  </div>
  <div class="cell" style="left:471px;top:0;height:182px;background:#fff;padding-left:48px;padding-right:4px">
    <h3 style="margin-bottom:4px">Sie möchten einen fixen A<br>nsprechpartner bei Problemen,<br>die Sie nicht mehr intern lösen<br>können?</h3>
    <p>Wir stellen Ihnen auf Wunsch vor<br>Ort (stunden wie tageweise) oder<br>auch via Hotline und E-Mail unsere<br>Dienstleistungen zur Verfügung.</p>
  </div>
  <div class="cell tint" style="left:0;top:182px;height:163px;padding-top:37px">
    <h3>Sie benötigen für grössere<br>Projekte wie eine Servermigration<br>Hilfe für Ihr Team vor Ort?</h3>
    <p>Wir unterstützen Ihre Mitarbeiter<br>vor Ort.</p>
  </div>
  <div class="cell cell-photo" style="left:236px;top:182px;height:163px" role="img" aria-label="Foto: drei Kollegen im Büro vor einem Laptop"></div>
  <div class="cell tint" style="left:472px;top:182px;height:163px;padding-top:37px">
    <h3>Sie möchten mehr<br>Dienstleistungen aus einer Hand?</h3>
    <p>Wir bieten Ihnen Backup, Hosted<br>Exchange E-Mail und Webhosting<br>inkl. Webdesign und weitere<br>massgeschneiderte Lösungen.</p>
  </div>
  <div class="cell" style="left:0;top:345px;height:137px;background:#fff;padding-top:34px">
    <h3>Sie möchten Ihre Daten schützen?</h3>
    <p>Wir zeigen Ihnen die wirksamsten<br>Möglichkeiten, wie Sie Ihre Daten<br>sichern gegen Diebstahl und<br>unbefugten Zugriff.</p>
  </div>
  <div class="cell tint" style="left:236px;top:345px;height:137px;padding-top:35px;padding-left:46px">
    <h3>Sie möchten Ihre IT Infrastruktur<br>betreuen lassen?</h3>
    <p>Wir betreuen und verwalten Ihre<br>Server und Netzinfrastruktur.</p>
  </div>
</section>

<section class="abs band">
  <p>Unseren <b>Flyer</b> können Sie hier herunterladen.</p>
  <div class="btn">Kontaktieren Sie uns jetzt</div>
</section>

<footer class="abs footer">
  <svg class="ficon" style="top:46px" width="20" height="24" viewBox="0 0 20 24" fill="none" stroke="#fff" stroke-width="1.6"><path d="M10 23s8-8 8-13a8 8 0 0 0-16 0c0 5 8 13 8 13z"/><circle cx="10" cy="10" r="3"/></svg>
  <div class="contact" style="top:45px"><b>NORVETA GmbH</b><br>Lindenweg 12<br>CH-4051 Basel</div>
  <svg class="ficon" style="top:100px" width="20" height="20" viewBox="0 0 24 24" fill="none" stroke="#fff" stroke-width="1.6"><path d="M5 3h4l2 5-2.5 1.5a11 11 0 0 0 6 6L16 13l5 2v4a2 2 0 0 1-2 2A16 16 0 0 1 3 5a2 2 0 0 1 2-2z"/></svg>
  <div class="contact" style="top:97px">Telefon<br>+41 61 000 4821</div>
  <svg class="ficon" style="top:141px" width="20" height="16" viewBox="0 0 24 18" fill="none" stroke="#fff" stroke-width="1.8"><rect x="1" y="1" width="22" height="16"/><path d="M1 2l11 8 11-8"/></svg>
  <div class="contact" style="top:138px">Email<br>support@norveta.ch</div>

  <div class="svc-head">LEISTUNGEN</div>
  <ul class="svc" style="left:404px;top:66px"><li>IT-Betreuung</li><li>IT-Sicherheit</li><li>Backup</li><li>Scientific IT</li></ul>
  <ul class="svc" style="left:510px;top:66px"><li>Websites</li><li>Raumbuchung</li><li>Coworking Space / Sitzungszimmer</li><li>Home Office Lösungen</li></ul>
  <ul class="svc" style="left:712px;top:66px"><li>Telefonie</li><li>Monitoring</li><li>Passwort Manager</li></ul>
</footer>

<div class="abs bottom">
  <div class="brand"><span>NORVETA</span><span class="dot"></span></div>
  <nav class="legal"><span>Newsletter</span><span>Datenschutz</span><span>AGB</span><span>Impressum</span></nav>
</div>
</body>
</html>
```